We need a website design for a new company called Studious Baguette. We offer :
- language tutoring for scholars or adult learners
- and other educational services associated with the French language as
*online support
*and immersive language cards games as card match, dominos, puzzle and happy family cards. Studious baguette will provide immersive and playful support to all age language learners.

Target Market(s)

Parents, French educators (teachers, tutors), Language schools, students

Industry/Entity Type

Tutoring

Coding

Coded - Design and coding required

Number of Pages Required

4 page

Requirements
Must have
• Clean and elegant design. Pages should be balanced and elements pleasingly presented
• Three buckets structure

```html
<!DOCTYPE html>
<html lang="en">
<head>
<meta charset="utf-8">
<title>Studious Baguette – French Tutoring &amp; Language Games</title>
<link href="https://fonts.googleapis.com/css2?family=Open+Sans:wght@400;600;700&family=Oswald:wght@500;600&display=swap" rel="stylesheet">
<style>
:root{
  --yellow:#f8b83a;--orange:#ec8a33;--magenta:#c12670;--plum:#9b1b58;
  --band:#a6427f;--teal:#2bbbc1;--ink:#3a3a3a;--muted:#8a8a8a;
  --grey:#efefef;--foot:#1e1e1e;--foot2:#171717;--gold:#f0a21f;
}
*{margin:0;padding:0;box-sizing:border-box}
html,body{width:1200px;height:3879px;overflow:hidden}
body{position:relative;font-family:"Open Sans",Arial,sans-serif;color:var(--ink);background:#fff}
.abs{position:absolute}
.hero{left:0;top:0;width:1200px;height:693px;background:linear-gradient(100deg,#f2e3c9 0%,#d8b98c 30%,#8b7a5a 60%,#c9b98a 85%,#e6dcc0 100%)}
.header{left:0;top:0;width:1200px;height:125px;background:rgba(255,255,255,.88)}
.logo{left:78px;top:28px;display:flex;align-items:center;gap:14px}
.logo .mark{width:46px;height:46px;border-radius:50%;background:var(--orange)}
.logo span{font-size:34px;font-weight:700;color:var(--plum);line-height:1}
.phone{left:686px;top:38px;font-size:17px;font-weight:600;display:flex;align-items:center;gap:8px}
.phone b{font-size:22px}
.login{left:967px;top:31px;width:176px;height:40px;background:#f4b400;color:#fff;font-size:15px;font-weight:600;text-align:center;line-height:40px}
.nav{top:92px;font-size:14px;font-weight:600;color:#333}
.bucket{top:755px;width:122px;height:186px}
.bucket svg{position:absolute;left:41px;top:115px}
.btitle{top:972px;width:280px;text-align:center;font-family:Oswald,sans-serif;font-size:20px;font-weight:500;color:#222}
.btext{top:1008px;width:270px;text-align:center;font-size:12.5px;line-height:20px;color:var(--muted)}
.band-l{left:0;top:1138px;width:1200px;height:238px}
.search-k{left:0;top:1168px;width:1200px;padding-left:260px;text-align:center;color:#fff}
.search-k small{display:block;font-size:17px;font-weight:700;letter-spacing:1px}
.search-k strong{display:block;font-size:34px;font-weight:700;letter-spacing:1px;margin-top:4px}
.sbox{left:388px;top:1267px;width:664px;height:52px;background:#fff;display:flex;font-size:14px;color:#999;align-items:center}
.sbox .cat{width:162px;padding-left:24px;border-right:1px solid #ddd;line-height:52px}
.sbox .q{padding-left:14px}
.sec-title{left:0;width:1200px;text-align:center;font-size:34px;font-weight:700;color:#3a3a3a;letter-spacing:1px}
.sec-sub{left:0;width:1200px;text-align:center;font-size:15px;color:var(--muted)}
.divider{left:500px;width:200px;height:20px}
.svc{top:1583px;width:240px;height:248px;border:1px solid #eee;background:#fff;text-align:center}
.svc.on{box-shadow:0 4px 16px rgba(0,0,0,.12)}
.svc svg{margin-top:44px}
.svc h3{margin-top:28px;font-size:15px;font-weight:700;color:#333}
.svc.on h3{color:var(--gold)}
.svc p{margin:14px 20px 0;font-size:13.5px;line-height:21px;color:var(--muted)}
.featured{left:0;top:1900px;width:1200px;height:595px;background:var(--grey)}
.course{top:2048px;width:342px}
.course .ph{height:189px;position:relative;border-bottom:6px solid var(--orange)}
.course .new{position:absolute;right:10px;top:12px;background:var(--orange);color:#fff;font-size:11px;font-weight:700;padding:3px 8px}
.course h4{margin-top:16px;font-size:21px;font-weight:600;color:#333}
.course .meta{margin-top:6px;font-size:11.5px;color:#555;display:flex;gap:26px}
.course .meta i{display:inline-block;width:10px;height:10px;background:var(--orange);border-radius:2px;margin-right:6px;vertical-align:-1px}
.course p{margin-top:14px;font-size:13px;line-height:21px;color:#666;height:64px;overflow:hidden}
.course .apply{margin-top:22px;width:134px;height:42px;background:var(--teal);color:#fff;font-size:12px;font-weight:700;text-align:center;line-height:42px}
.nl-title{left:190px;top:3165px;font-family:Oswald,sans-serif;font-size:36px;font-weight:600;line-height:38px;color:#fff;letter-spacing:1px}
.nl-input{left:525px;top:3196px;width:556px;height:49px;background:#fff;font-size:12px;color:#888;line-height:49px;padding-left:40px;letter-spacing:1px}
.nl-btn{left:1081px;top:3196px;width:56px;height:49px;background:#8b45a0}
.footer{left:0;top:3277px;width:1200px;height:550px;background:var(--foot)}
.flogo{left:0;top:3300px;width:1200px;display:flex;justify-content:center;align-items:center;gap:12px}
.flogo .mark{width:36px;height:36px;border-radius:50%;background:#777}
.flogo span{font-size:30px;font-weight:700;color:#9a9a9a}
.fdesc{left:320px;top:3372px;width:560px;text-align:center;font-size:13px;line-height:26px;color:#888}
.soc{top:3445px;width:32px;height:32px;border-radius:50%;background:#3a3a3a}
.fh{top:3535px;font-size:15px;font-weight:700;color:var(--gold)}
.fh::after{content:"";display:block;width:28px;height:2px;background:var(--gold);margin-top:8px}
.contact{left:54px;top:3590px;width:240px;font-size:12px;line-height:20px;color:#aaa}
.contact li{list-style:none;margin-bottom:6px;padding-left:18px;position:relative}
.contact li::before{content:"";position:absolute;left:2px;top:7px;width:6px;height:6px;border-radius:50%;background:#888}
.tags{left:331px;top:3590px;width:230px;display:flex;flex-wrap:wrap;gap:8px}
.tags span{border:1px solid #555;color:#aaa;font-size:10px;padding:6px 8px;letter-spacing:.5px}
.news{left:608px;width:230px;display:flex;gap:12px}
.news .th{width:48px;height:48px;background:linear-gradient(135deg,#8a7a5a,#c8b390);flex:none}
.news b{display:block;font-size:12px;color:#fff;line-height:18px;font-weight:600}
.news small{font-size:10px;color:#888}
.ask{left:884px;width:250px;border:1px solid #444;font-size:11px;color:#888;padding-left:12px;letter-spacing:1px}
.send{left:884px;top:3700px;width:116px;height:36px;background:var(--teal);color:#fff;font-size:11px;font-weight:700;text-align:center;line-height:36px}
.bottom{left:0;top:3827px;width:1200px;height:52px;background:var(--foot2);font-size:11px;color:#aaa;line-height:52px}
.bottom a{position:absolute;color:#aaa;text-decoration:none}
</style>
</head>
<body>

<div class="abs hero" role="img" aria-label="Photo of a smiling graduate in cap and glasses with classmates celebrating outdoors"></div>

<header class="abs header">
  <div class="abs logo"><div class="mark"></div><span>Studious Baguette</span></div>
  <div class="abs phone">
    <svg width="18" height="18" viewBox="0 0 24 24"><path d="M6.6 10.8a15 15 0 006.6 6.6l2.2-2.2c.3-.3.7-.4 1-.2 1.1.4 2.3.6 3.6.6.6 0 1 .4 1 1V20c0 .6-.4 1-1 1A17 17 0 013 4c0-.6.4-1 1-1h3.5c.6 0 1 .4 1 1 0 1.3.2 2.5.6 3.6.1.3 0 .7-.2 1z" fill="#333"/></svg>
    Call us on <b>1800-555-0199</b>
  </div>
  <div class="abs login">STUDENTS LOGIN</div>
  <nav>
    <span class="abs nav" style="left:500px">HOME</span>
    <span class="abs nav" style="left:582px">ABOUT US</span>
    <span class="abs nav" style="left:693px">COURSES</span>
    <span class="abs nav" style="left:796px">NEWS</span>
    <span class="abs nav" style="left:877px">STUDY</span>
    <span class="abs nav" style="left:962px">CAREERS</span>
    <span class="abs nav" style="left:1063px">CONTACT US</span>
  </nav>
</header>

<section class="buckets">
  <div class="abs bucket" style="left:129px;background:var(--yellow)"><svg width="40" height="40" viewBox="0 0 24 24"><path d="M12 4L1 9l11 5 9-4.1V16h2V9L12 4zM5 13.2v4L12 21l7-3.8v-4L12 17l-7-3.8z" fill="#fff"/></svg></div>
  <div class="abs bucket" style="left:406px;background:var(--orange)"><svg width="40" height="40" viewBox="0 0 24 24"><path d="M3 17.2V21h3.8L17.8 9.9l-3.8-3.8L3 17.2zM20.7 7a1 1 0 000-1.4l-2.3-2.3a1 1 0 00-1.4 0l-1.8 1.8 3.8 3.8L20.7 7z" fill="#fff"/></svg></div>
  <div class="abs bucket" style="left:680px;background:var(--magenta)"><svg width="40" height="40" viewBox="0 0 24 24"><circle cx="10" cy="10" r="6" fill="none" stroke="#fff" stroke-width="2.6"/><path d="M14.5 14.5L20 20" stroke="#fff" stroke-width="3" stroke-linecap="round"/></svg></div>
  <div class="abs bucket" style="left:957px;background:var(--plum)"><svg width="40" height="40" viewBox="0 0 24 24"><circle cx="12" cy="12" r="6" fill="#fff"/><g stroke="#fff" stroke-width="2.4"><path d="M12 3v18M3 12h18M5.6 5.6l12.8 12.8M18.4 5.6L5.6 18.4"/></g></svg></div>

  <h3 class="abs btitle" style="left:50px">BE PART OF US</h3>
  <h3 class="abs btitle" style="left:327px">BROWSE COURSES</h3>
  <h3 class="abs btitle" style="left:601px">FIND TEACHERS</h3>
  <h3 class="abs btitle" style="left:878px">GET CERTIFICATION</h3>
  <p class="abs btext" style="left:55px">Join young scholars and adult learners who study French with a tutor, at their own pace.</p>
  <p class="abs btext" style="left:332px">Explore French courses for every level, from first words to fluent everyday talk.</p>
  <p class="abs btext" style="left:606px">Meet French tutors who guide each lesson with patience, care and playful games.</p>
  <p class="abs btext" style="left:883px">Prepare for DELF exams with mock tests, clear feedback and steady online support.</p>
</section>

<section class="search">
  <svg class="abs band-l" width="1200" height="238" viewBox="0 0 1200 238">
    <rect width="1200" height="238" fill="var(--orange)"/>
    <polygon points="225,0 1200,0 1200,238 300,238 220,80" fill="var(--band)"/>
  </svg>
  <div class="abs search-k"><small>SEARCH FOR</small><strong>ALL COURSE</strong></div>
  <div class="abs sbox"><div class="cat">ALL CATEGORY ⌄</div><div class="q">ENTER COURSES NAME</div></div>
</section>

<section class="services">
  <h2 class="abs sec-title" style="top:1426px">BEST SERVICES</h2>
  <p class="abs sec-sub" style="top:1482px">Immersive and playful French support for learners of all ages</p>
  <svg class="abs divider" style="top:1520px" viewBox="0 0 200 20"><path d="M10 10h70M120 10h70" stroke="#333" stroke-width="2"/><path d="M100 4l10 4-10 4-10-4z" fill="#333"/><path d="M94 11v4l6 3 6-3v-4" fill="#333"/></svg>

  <div class="abs svc on" style="left:65px">
    <svg width="56" height="56" viewBox="0 0 56 56" fill="none" stroke="var(--gold)" stroke-width="2"><ellipse cx="28" cy="28" rx="24" ry="9"/><ellipse cx="28" cy="28" rx="24" ry="9" transform="rotate(60 28 28)"/><ellipse cx="28" cy="28" rx="24" ry="9" transform="rotate(-60 28 28)"/><circle cx="28" cy="28" r="3" fill="var(--gold)"/></svg>
    <h3>FRENCH TUTORING</h3><p>One to one lessons for scholars and adults, built around each goal.</p>
  </div>
  <div class="abs svc" style="left:336px">
    <svg width="56" height="56" viewBox="0 0 56 56" fill="none" stroke="#333" stroke-width="2"><circle cx="28" cy="20" r="11"/><path d="M8 52c2-12 10-18 20-18s18 6 20 18"/></svg>
    <h3>ONLINE SUPPORT</h3><p>Tutors answer questions and check homework online, any day.</p>
  </div>
  <div class="abs svc" style="left:608px">
    <svg width="56" height="56" viewBox="0 0 56 56" fill="none" stroke="#333" stroke-width="2"><circle cx="28" cy="28" r="24"/><circle cx="28" cy="28" r="19"/><path d="M36 20l-5 11-11 5 5-11z"/></svg>
    <h3>CARD MATCH &amp; DOMINOS</h3><p>Word games that turn new French vocabulary into quick wins.</p>
  </div>
  <div class="abs svc" style="left:879px">
    <svg width="56" height="56" viewBox="0 0 56 56" fill="none" stroke="#333" stroke-width="2"><rect x="4" y="12" width="48" height="34"/><path d="M28 4v50M4 29h48"/><rect x="20" y="22" width="16" height="14"/></svg>
    <h3>PUZZLES &amp; HAPPY FAMILY</h3><p>Card sets that let the whole family play and speak French.</p>
  </div>
</section>

<section class="abs featured"></section>
<h2 class="abs sec-title" style="top:1915px">FEATURED COURSES</h2>
<p class="abs sec-sub" style="top:1970px">French lessons and language games for every kind of learner</p>
<svg class="abs divider" style="top:2008px" viewBox="0 0 200 20"><path d="M10 10h70M120 10h70" stroke="#333" stroke-width="2"/><path d="M100 4l10 4-10 4-10-4z" fill="#333"/><path d="M94 11v4l6 3 6-3v-4" fill="#333"/></svg>

<article class="abs course" style="left:59px">
  <div class="ph" role="img" aria-label="Photo of three students standing in front of a chalkboard with doodles" style="background:linear-gradient(135deg,#2e2e2e,#5a5a5a)"><span class="new">NEW</span></div>
  <h4>French for Young Scholars</h4>
  <div class="meta"><span><i></i>2M 3H</span><span><i></i>CLAIRE MARTIN</span><span><i></i>BEGINNER</span></div>
  <p>Weekly lessons that help children read, write and speak French with confidence, using songs, stories and card match games to fix new words.</p>
  <div class="apply">APPLY NOW</div>
</article>
<article class="abs course" style="left:429px">
  <div class="ph" role="img" aria-label="Photo of hands sketching a layout on paper at a wooden desk" style="background:linear-gradient(135deg,#b49a78,#e8dccb)"><span class="new">NEW</span></div>
  <h4>Adult Conversation Club</h4>
  <div class="meta"><span><i></i>2M 3H</span><span><i></i>CLAIRE MARTIN</span><span><i></i>BEGINNER</span></div>
  <p>Small group sessions for adult learners who want to speak French for travel or work, with online support between classes to keep progress going.</p>
  <div class="apply">APPLY NOW</div>
</article>
<article class="abs course" style="left:799px">
  <div class="ph" role="img" aria-label="Photo of smiling students sitting together in a classroom" style="background:linear-gradient(135deg,#c9b08a,#7a5e44)"><span class="new">NEW</span></div>
  <h4>Language Card Games</h4>
  <div class="meta"><span><i></i>2M 2H</span><span><i></i>CLAIRE MARTIN</span><span><i></i>BEGINNER</span></div>
  <p>Play dominos, puzzles and happy family cards in French. A playful course for schools, tutors and parents who want learning to feel like a game.</p>
  <div class="apply">APPLY NOW</div>
</article>

<section class="gallery">
  <h2 class="abs sec-title" style="top:2522px">STUDENT GALLERY</h2>
  <p class="abs sec-sub" style="top:2577px">Our learners reading, playing and speaking French together</p>
  <svg class="abs divider" style="top:2615px" viewBox="0 0 200 20"><path d="M10 10h70M120 10h70" stroke="#333" stroke-width="2"/><path d="M100 4l10 4-10 4-10-4z" fill="#333"/><path d="M94 11v4l6 3 6-3v-4" fill="#333"/></svg>
  <div class="abs" role="img" aria-label="Photo of students holding notebooks" style="left:47px;top:2677px;width:181px;height:155px;background:linear-gradient(135deg,#5d8a3c,#d6b06a)"></div>
  <div class="abs" role="img" aria-label="Photo of a student at a desk" style="left:47px;top:2858px;width:181px;height:155px;background:linear-gradient(135deg,#a08670,#e0d4c8)"></div>
  <div class="abs" role="img" aria-label="Photo of a group of students giving thumbs up, with yellow overlay" style="left:248px;top:2677px;width:349px;height:336px;background:linear-gradient(135deg,#f0c23a,#d9a42a)">
    <svg class="abs" style="left:150px;top:144px" width="48" height="48" viewBox="0 0 48 48"><circle cx="24" cy="24" r="24" fill="rgba(255,255,255,.5)"/><circle cx="22" cy="22" r="9" fill="none" stroke="#333" stroke-width="3"/><path d="M29 29l7 7M18 22h8M22 18v8" stroke="#333" stroke-width="3"/></svg>
  </div>
  <div class="abs" role="img" aria-label="Photo of students studying together in a library" style="left:616px;top:2677px;width:336px;height:336px;background:linear-gradient(135deg,#6b4a35,#c7a88a)"></div>
  <div class="abs" role="img" aria-label="Photo of a student reading between bookshelves" style="left:972px;top:2677px;width:181px;height:155px;background:linear-gradient(135deg,#4d5a7a,#b89070)"></div>
  <div class="abs" role="img" aria-label="Photo of a student writing in a notebook" style="left:972px;top:2858px;width:181px;height:155px;background:linear-gradient(135deg,#f2c54a,#c79a5a)"></div>
</section>

<section class="newsletter">
  <svg class="abs" style="left:0;top:3129px" width="1200" height="148" viewBox="0 0 1200 148">
    <rect width="1200" height="148" fill="var(--orange)"/>
    <polygon points="0,0 400,0 450,148 0,148" fill="var(--band)"/>
    <g fill="none" stroke="var(--yellow)" stroke-width="5"><rect x="60" y="40" width="80" height="56" transform="rotate(-20 100 68)"/><path d="M63 50l40 26 38-40" transform="rotate(-8 100 68)"/></g>
  </svg>
  <div class="abs nl-title">OUR<br>NEWSLETTER</div>
  <div class="abs nl-input">ENTER YOUR E-MAIL ADDRESS</div>
  <div class="abs nl-btn"><svg width="56" height="49" viewBox="0 0 56 49"><path d="M18 26l22-10-8 20-4-7z" fill="#fff"/></svg></div>
</section>

<footer>
  <div class="abs footer"></div>
  <div class="abs flogo"><div class="mark"></div><span>Studious Baguette</span></div>
  <p class="abs fdesc">French tutoring, online support and immersive card games for scholars, adults and families learning French.</p>
  <div class="abs soc" style="left:489px"></div>
  <div class="abs soc" style="left:529px"></div>
  <div class="abs soc" style="left:569px"></div>
  <div class="abs soc" style="left:609px"></div>
  <div class="abs soc" style="left:649px"></div>
  <div class="abs soc" style="left:689px"></div>

  <h4 class="abs fh" style="left:54px">GET IN TOUCH</h4>
  <h4 class="abs fh" style="left:331px">POPULAR TAGS</h4>
  <h4 class="abs fh" style="left:608px">LATEST NEWS</h4>
  <h4 class="abs fh" style="left:884px">ASK A QUESTION</h4>

  <ul class="abs contact">
    <li>Studio 12, 48 Rue des Lilas, Lyon, France (69003)</li>
    <li>(+33) 555-010-222</li>
    <li>hello@studiousmail.com</li>
  </ul>

  <div class="abs tags">
    <span>FRENCH</span><span>KIDS</span><span>VOCABULARY</span><span>DOMINOS</span><span>E-LEARNING</span><span>ADULTS</span><span>CARD MATCH</span><span>DELF</span><span>PUZZLE</span><span>ONLINE SUPPORT</span><span>HAPPY FAMILY</span><span>GRAMMAR</span><span>TUTORS</span>
  </div>

  <div class="abs news" style="top:3590px"><div class="th" role="img" aria-label="News thumbnail photo"></div><div><b>New Happy Family Card Deck for French Beginners</b><small>NOVEMBER 3, 2015</small></div></div>
  <div class="abs news" style="top:3670px"><div class="th" role="img" aria-label="News thumbnail photo"></div><div><b>How Card Games Help Children Learn French</b><small>AUGUST 1, 2015</small></div></div>

  <div class="abs ask" style="top:3580px;height:36px;line-height:36px">EMAIL ADDRESS</div>
  <div class="abs ask" style="top:3628px;height:56px;line-height:30px">QUESTION</div>
  <div class="abs send">SEND NOW</div>

  <div class="abs bottom">
    <a style="left:54px">HOME</a><a style="left:124px">COURSE</a><a style="left:204px">EVENTS</a><a style="left:282px">BLOG</a><a style="left:350px">ABOUT</a>
    <span class="abs" style="right:54px">© 2016 - STUDIOUS BAGUETTE</span>
  </div>
</footer>

</body>
</html>
```